Business Cards

Need a neat design for a new business card

Industry/Entity Type

Residential Construction

Contact Information for Business Card

Company Name- KOVE Construction Inc.
Owner- Marcus Tolliver
Phone number- (555)203-7481
Email- kovecohomes@brindlemail.example
Facebook- www.socialpage.example/kovecohomes

Colors
fefdec

```html
<!DOCTYPE html>
<html lang="en">
<head>
<meta charset="utf-8">
<title>KOVE Construction Inc. – Business Card</title>
<link rel="stylesheet" href="https://fonts.googleapis.com/css2?family=Arimo:wght@400;700&display=swap">
<style>
  :root {
    --backdrop: #b8b8b8;
    --card-light: #ffffff;
    --card-dark: #000000;
    --ink: #111111;
    --ink-reverse: #ffffff;
  }
  * { margin: 0; padding: 0; box-sizing: border-box; }
  html, body {
    width: 1200px;
    height: 801px;
    overflow: hidden;
    background: var(--backdrop);
    font-family: "Arimo", Arial, sans-serif;
  }
  .canvas { position: relative; width: 1200px; height: 801px; }
  .card {
    position: absolute;
    top: 274px;
    width: 443px;
    height: 262px;
  }
  .card--front { left: 153px; background: var(--card-light); color: var(--ink); }
  .card--back { left: 625px; background: var(--card-dark); color: var(--ink-reverse); }

  .holder { position: absolute; left: 22px; top: 31px; }
  .holder__name { font-size: 15px; font-weight: 700; letter-spacing: 0.2px; line-height: 1; }
  .holder__role { font-size: 11.5px; font-weight: 400; margin-top: 4px; line-height: 1; }

  .front-mark {
    position: absolute;
    left: 210px;
    top: 108px;
    font-size: 54px;
    font-weight: 700;
    letter-spacing: 3px;
    line-height: 1;
    color: var(--ink);
  }

  .contacts {
    position: absolute;
    left: 22px;
    top: 191px;
    list-style: none;
    font-size: 12px;
    line-height: 15.5px;
  }
  .contacts__item { display: flex; align-items: center; gap: 6px; }
  .contacts__icon { width: 10px; height: 10px; flex: none; }

  .back-mark {
    position: absolute;
    inset: 0;
    display: flex;
    align-items: center;
    justify-content: center;
  }
  .back-mark__name {
    font-size: 22px;
    font-weight: 400;
    letter-spacing: 2.5px;
    color: var(--ink-reverse);
  }
</style>
</head>
<body>
<main class="canvas">
  <section class="card card--front" aria-label="Business card front">
    <div class="holder">
      <p class="holder__name">MARCUS TOLLIVER</p>
      <p class="holder__role">OWNER</p>
    </div>

    <p class="front-mark">KOVE</p>

    <ul class="contacts">
      <li class="contacts__item">
        <svg class="contacts__icon" viewBox="0 0 10 10" aria-hidden="true">
          <path d="M2 0.8 L3.6 2.8 L2.8 3.8 C3.4 5.2 4.6 6.5 6.1 7.2 L7.1 6.4 L9.2 8 L8.2 9.4 C4.4 9.2 0.8 5.6 0.6 1.8 Z" fill="currentColor"/>
        </svg>
        <span>(555)203-7481</span>
      </li>
      <li class="contacts__item">
        <svg class="contacts__icon" viewBox="0 0 10 10" aria-hidden="true">
          <rect x="0.5" y="2" width="9" height="6.2" fill="currentColor"/>
          <path d="M0.8 2.3 L5 5.6 L9.2 2.3" fill="none" stroke="#fff" stroke-width="0.9"/>
        </svg>
        <span>kovecohomes@brindlemail.example</span>
      </li>
      <li class="contacts__item">
        <svg class="contacts__icon" viewBox="0 0 10 10" aria-hidden="true">
          <circle cx="5" cy="5" r="3.6" fill="currentColor"/>
        </svg>
        <span>www.socialpage.example/kovecohomes</span>
      </li>
    </ul>
  </section>

  <section class="card card--back" aria-label="Business card back">
    <div class="back-mark">
      <p class="back-mark__name">KOVE CONSTRUCTION INC.</p>
    </div>
  </section>
</main>
</body>
</html>
```